Create banner ads for a digital product that deletes personal information from the web

The context of the banners is general advertisement for our service.
Please provide us with a set of static and flash/gif banners in the following standard sizes for the theme you create:
160x600
300x250
300x600
320x250
336x280
728x90
Please see our website for logo (just our name) and theme ideas - please follow similar color/font schemes if possible. www.quillbarrow.com
Our company is an online service that deletes personal information from the internet for our members (automated opt-outs and content removal). Our target audience is anyone who wishes to protect their personal information from being on the internet (i.e. prefer to fly under the internet radar, for example). This is a product for U.S. residents who value privacy and online reputation. We seek to provide members with control of what 300+ websites are sharing about them – removing names, addresses, ages, phone numbers, email addresses, children’s information, home/property value information etc.

```html
<!DOCTYPE html>
<html lang="en">
<head>
<meta charset="utf-8">
<title>Quillbarrow – Online Privacy Service Banners</title>
<link rel="stylesheet" href="https://fonts.googleapis.com/css2?family=Special+Elite&family=Didact+Gothic&family=Arimo:wght@400&display=swap">
<style>
  :root {
    --page: #ffffff;
    --ink: #3a3a38;
    --ink-soft: #8a8955;
    --panel: #d6d78f;
    --photo-top: #d9d8b4;
    --photo-bottom: #b3bf80;
    --icon-fill: rgba(238, 238, 232, 0.92);
    --icon-ring: #c9c9c0;
    --icon-ink: #4a4a48;
    --url: #111111;
  }
  * { box-sizing: border-box; margin: 0; padding: 0; }
  html, body {
    width: 1200px;
    height: 1002px;
    overflow: hidden;
    background: var(--page);
  }
  .canvas {
    position: relative;
    width: 1200px;
    height: 1002px;
  }
  .banner { position: absolute; overflow: hidden; }

  .photo-area {
    position: absolute;
    inset: 0;
    background: linear-gradient(180deg, var(--photo-top) 0%, var(--photo-bottom) 100%);
  }

  .brand-name {
    position: absolute;
    font-family: "Special Elite", "Courier New", monospace;
    font-weight: 400;
    color: var(--ink);
    white-space: nowrap;
    line-height: 1;
  }
  .tagline {
    position: absolute;
    font-family: "Didact Gothic", "Century Gothic", sans-serif;
    font-weight: 400;
    white-space: nowrap;
    line-height: 1;
  }
  .site-url {
    position: absolute;
    font-family: "Arimo", Arial, sans-serif;
    color: var(--url);
    white-space: nowrap;
    line-height: 1;
  }

  .icon-row { position: absolute; display: flex; }
  .icon-badge {
    border-radius: 50%;
    background: var(--icon-fill);
    border: 2px solid var(--icon-ring);
    display: flex;
    align-items: center;
    justify-content: center;
  }
  .icon-badge svg { width: 56%; height: 56%; fill: var(--icon-ink); }

  /* Medium rectangle 300x250 at 1.5x */
  .rectangle { left: 375px; top: 212px; width: 450px; height: 375px; }
  .rectangle .brand-name { left: 12px; top: 16px; font-size: 60px; }
  .rectangle .tagline { color: var(--ink); font-size: 45px; }
  .rectangle .tagline-line1 { left: 20px; top: 108px; }
  .rectangle .tagline-line2 { left: 0; width: 100%; text-align: center; top: 176px; padding-left: 14px; }
  .rectangle .icon-row { left: 10px; top: 252px; gap: 9px; }
  .rectangle .icon-badge { width: 63px; height: 63px; }
  .rectangle .site-url { left: 0; width: 100%; text-align: center; top: 340px; font-size: 24px; }

  /* Leaderboard 728x90 at 1.5x */
  .leaderboard { left: 54px; top: 654px; width: 1092px; height: 135px; }
  .leaderboard .brand-panel {
    position: absolute; left: 0; top: 0; width: 444px; height: 100%;
    background: var(--panel);
  }
  .leaderboard .photo-area { left: 444px; }
  .leaderboard .brand-name { left: 10px; top: 12px; font-size: 57px; }
  .leaderboard .tagline { left: 10px; top: 80px; font-size: 37px; color: var(--ink-soft); }
  .leaderboard .icon-row { left: 478px; top: 20px; gap: 9px; }
  .leaderboard .icon-badge { width: 60px; height: 60px; }
  .leaderboard .site-url { left: 530px; top: 96px; font-size: 27px; }
</style>
</head>
<body>
<main class="canvas">

  <section class="banner rectangle" aria-label="Quillbarrow medium rectangle banner">
    <div class="photo-area" role="img" aria-label="Photo placeholder: person with raised arms in a sunlit grassy field"></div>
    <h1 class="brand-name">Quillbarrow</h1>
    <p class="tagline tagline-line1">Online Privacy</p>
    <p class="tagline tagline-line2">Service</p>
    <div class="icon-row">
      <span class="icon-badge"><svg viewBox="0 0 24 24"><circle cx="12" cy="7" r="3"/><path d="M6.5 18c0-3.4 2.5-6 5.5-6s5.5 2.6 5.5 6z"/><circle cx="5" cy="9" r="2.2"/><path d="M0.8 17c0-2.7 1.9-4.8 4.2-4.8 1 0 1.9.4 2.6 1-1 1.1-1.6 2.4-1.8 3.8z"/><circle cx="19" cy="9" r="2.2"/><path d="M23.2 17c0-2.7-1.9-4.8-4.2-4.8-1 0-1.9.4-2.6 1 1 1.1 1.6 2.4 1.8 3.8z"/></svg></span>
      <span class="icon-badge"><svg viewBox="0 0 24 24"><path d="M7 10V7a5 5 0 0 1 10 0v3h-2V7a3 3 0 0 0-6 0v3z"/><path d="M5 10h14v12H5zm6 4v4h2v-4z" fill-rule="evenodd"/></svg></span>
      <span class="icon-badge"><svg viewBox="0 0 24 24"><path d="M6.6 10.8a15.2 15.2 0 0 0 6.6 6.6l2.2-2.2c.3-.3.7-.4 1-.2 1.1.4 2.3.6 3.6.6.6 0 1 .4 1 1V20c0 .6-.4 1-1 1A17 17 0 0 1 3 4c0-.6.4-1 1-1h3.5c.6 0 1 .4 1 1 0 1.3.2 2.5.6 3.6.1.3 0 .7-.2 1z"/></svg></span>
      <span class="icon-badge"><svg viewBox="0 0 24 24"><path d="M2 5h20v14H2zm2 2v.5l8 5.5 8-5.5V7zm0 3v7h16v-7l-8 5.5z" fill-rule="evenodd"/></svg></span>
      <span class="icon-badge"><svg viewBox="0 0 24 24"><path d="M5 2h14v20H5zm2 2v16h10V4zm1.5 2h7v1.5h-7zm0 3h7v1.5h-7zm0 3h7v1.5h-7zm0 3h7v1.5h-7z" fill-rule="evenodd"/></svg></span>
      <span class="icon-badge"><svg viewBox="0 0 24 24"><path d="M9 2h6v2h5v2H4V4h5zM5 7h14l-1 15H6zm3 2v11h1.6V9zm3.2 0v11h1.6V9zm3.2 0v11H16V9z" fill-rule="evenodd"/></svg></span>
    </div>
    <p class="site-url">www.quillbarrow.com</p>
  </section>

  <section class="banner leaderboard" aria-label="Quillbarrow leaderboard banner">
    <div class="brand-panel"></div>
    <div class="photo-area" role="img" aria-label="Photo placeholder: person with raised arms in a sunlit grassy field"></div>
    <h2 class="brand-name">Quillbarrow</h2>
    <p class="tagline">Online Privacy Service</p>
    <div class="icon-row">
      <span class="icon-badge"><svg viewBox="0 0 24 24"><circle cx="12" cy="7" r="3"/><path d="M6.5 18c0-3.4 2.5-6 5.5-6s5.5 2.6 5.5 6z"/><circle cx="5" cy="9" r="2.2"/><path d="M0.8 17c0-2.7 1.9-4.8 4.2-4.8 1 0 1.9.4 2.6 1-1 1.1-1.6 2.4-1.8 3.8z"/><circle cx="19" cy="9" r="2.2"/><path d="M23.2 17c0-2.7-1.9-4.8-4.2-4.8-1 0-1.9.4-2.6 1 1 1.1 1.6 2.4 1.8 3.8z"/></svg></span>
      <span class="icon-badge"><svg viewBox="0 0 24 24"><path d="M7 10V7a5 5 0 0 1 10 0v3h-2V7a3 3 0 0 0-6 0v3z"/><path d="M5 10h14v12H5zm6 4v4h2v-4z" fill-rule="evenodd"/></svg></span>
      <span class="icon-badge"><svg viewBox="0 0 24 24"><path d="M6.6 10.8a15.2 15.2 0 0 0 6.6 6.6l2.2-2.2c.3-.3.7-.4 1-.2 1.1.4 2.3.6 3.6.6.6 0 1 .4 1 1V20c0 .6-.4 1-1 1A17 17 0 0 1 3 4c0-.6.4-1 1-1h3.5c.6 0 1 .4 1 1 0 1.3.2 2.5.6 3.6.1.3 0 .7-.2 1z"/></svg></span>
      <span class="icon-badge"><svg viewBox="0 0 24 24"><path d="M2 5h20v14H2zm2 2v.5l8 5.5 8-5.5V7zm0 3v7h16v-7l-8 5.5z" fill-rule="evenodd"/></svg></span>
      <span class="icon-badge"><svg viewBox="0 0 24 24"><path d="M5 2h14v20H5zm2 2v16h10V4zm1.5 2h7v1.5h-7zm0 3h7v1.5h-7zm0 3h7v1.5h-7zm0 3h7v1.5h-7z" fill-rule="evenodd"/></svg></span>
      <span class="icon-badge"><svg viewBox="0 0 24 24"><path d="M9 2h6v2h5v2H4V4h5zM5 7h14l-1 15H6zm3 2v11h1.6V9zm3.2 0v11h1.6V9zm3.2 0v11H16V9z" fill-rule="evenodd"/></svg></span>
    </div>
    <p class="site-url">www.quillbarrow.com</p>
  </section>

</main>
</body>
</html>
```